Consulting Practice for Charities Needs A Brochure Deisgn

Hi! We need a tri-fold brochure for a Washington, DC based consulting practice that works with charities (NGOs, Associations, etc.) and wealthy donors (philanthropists). Our company, Brennick Civic Advisors, helps nonprofits to implement practices that maximize organizational efficiency and effectiveness - by working directly with board members and staff.
Our clients are well educated and quite sophisticated (some charities are international with multi-million dollar budgets, while others are quite local and small) This brochure will be handed to them by some of our 'referral partners' (law firms, accountants and even governmental agencies) in addition to being given out during our presentations. We draw inspiration from nature and would like to somehow include a "natural / eco-friendly" feel to the piece, including natural colors .... that being said, not in any way "folksy" - it must be sophisticated.

Target Market(s)

nonprofit executive directors, board chairs, wealth holders (philanthropists)

Industry/Entity Type

Consulting

Requirements
Must have
• I uploaded a word file with content (text) - most of that needs to be on the brochure ... but ... if it looks too crowded, let me know and I'll reduce
Nice to have
• pop-out quotes (maybe from testimonials??), nature - theme of some kind but also photo of boardroom (links to samples are like are uploaded in a word doc below)
Should not have
• nothing cute ... nothing too feminine

```html
<!DOCTYPE html>
<html lang="en">
<head>
<meta charset="utf-8">
<title>Brennick Civic Advisors – Brochure</title>
<link rel="stylesheet" href="https://fonts.googleapis.com/css2?family=Libre+Bodoni:wght@400;500&family=EB+Garamond:ital@0;1&display=swap">
<style>
  :root {
    --paper: #ffffff;
    --ink: #111111;
    --ink-reverse: #ffffff;
    --rule: #c9c9cf;
    --brand: #6b5ba8;
    --photo-light: #f2f3f4;
    --photo-mid: #d4d8db;
    --photo-dark: #8a8f96;
  }
  * { box-sizing: border-box; margin: 0; padding: 0; }
  html, body { width: 1200px; height: 518px; overflow: hidden; background: var(--paper); }
  .brochure { position: relative; width: 1200px; height: 518px; overflow: hidden; background: var(--paper); font-family: "Libre Bodoni", "Bodoni Moda", serif; color: var(--ink); }

  /* Cover panel */
  .cover { position: absolute; left: 0; top: 0; width: 400px; height: 518px; background: var(--paper); }
  .cover-rules { position: absolute; inset: 0; }
  .brand { position: absolute; left: 95px; top: 186px; width: 200px; text-align: center; font-family: "EB Garamond", serif; }
  .brand-mark { display: inline-flex; align-items: center; gap: 6px; font-size: 26px; color: var(--brand); letter-spacing: 1px; line-height: 1; }
  .brand-mark .square { width: 9px; height: 9px; background: var(--brand); }
  .brand-name, .brand-tagline { font-style: italic; font-size: 9.6px; line-height: 12px; color: var(--ink); }
  .brand-name { margin-top: 28px; }

  /* Inside spread */
  .boardroom-photo { position: absolute; left: 400px; top: 0; width: 800px; height: 518px;
    background:
      radial-gradient(ellipse 180px 200px at 120px 300px, rgba(40,50,70,.75), transparent 70%),
      radial-gradient(ellipse 110px 140px at 370px 260px, rgba(150,30,70,.55), transparent 70%),
      radial-gradient(ellipse 120px 200px at 760px 260px, rgba(30,30,40,.7), transparent 70%),
      linear-gradient(180deg, var(--photo-mid) 0%, var(--photo-light) 55%, #e9e6e1 100%); }

  .panel { position: absolute; font-size: 8.2px; line-height: 11.7px; }
  .panel p { text-indent: 8px; }
  .panel-dark { background: var(--ink); color: var(--ink-reverse); }
  .panel-light { background: var(--paper); color: var(--ink); }
  .heading { display: flex; align-items: center; justify-content: center; text-align: center; font-weight: 400; }

  .who-title { left: 565px; top: 0; width: 136px; height: 132px; font-size: 19px; }
  .founded { left: 666px; top: 134px; width: 134px; height: 134px; padding: 18px 8px 0 12px; }
  .team { left: 530px; top: 195px; width: 136px; height: 151px; padding: 25px 8px 0 10px; }
  .services { left: 578px; top: 346px; width: 192px; height: 172px; padding: 32px 10px 0 22px; }
  .services ul { list-style: none; }
  .services li { text-indent: 2px; }
  .services li::before { content: "•"; margin-right: 4px; }

  .what-title { position: absolute; left: 818px; top: 76px; font-size: 21px; font-weight: 400; }
  .quote { left: 837px; top: 110px; width: 144px; height: 116px; padding: 26px 10px 0 14px; }
  .org-label { left: 982px; top: 86px; width: 95px; height: 76px; font-size: 9.6px; line-height: 12.5px; align-items: flex-start; padding-top: 27px; }
  .believe { left: 891px; top: 226px; width: 210px; height: 150px; padding: 24px 14px 0 14px; }
  .private-label { left: 810px; top: 377px; width: 80px; height: 80px; font-size: 9.6px; }
  .individuals { left: 890px; top: 416px; width: 157px; height: 96px; padding: 38px 10px 0 14px; }
</style>
</head>
<body>
<main class="brochure">
  <section class="cover">
    <svg class="cover-rules" width="400" height="518" aria-hidden="true">
      <g stroke="var(--rule)" stroke-width="1">
        <line x1="122" y1="0" x2="122" y2="518"/>
        <line x1="134" y1="0" x2="134" y2="518"/>
        <line x1="146" y1="0" x2="146" y2="518"/>
        <line x1="166" y1="0" x2="166" y2="518"/>
        <line x1="186" y1="0" x2="186" y2="518"/>
        <line x1="210" y1="0" x2="210" y2="518"/>
        <line x1="234" y1="0" x2="234" y2="518"/>
        <line x1="254" y1="0" x2="254" y2="518"/>
        <line x1="276" y1="0" x2="276" y2="518"/>
      </g>
    </svg>
    <div class="brand">
      <div class="brand-mark"><span class="square"></span>BCA</div>
      <p class="brand-name">Brennick Civic Advisors</p>
      <p class="brand-tagline">Changing the culture of philanthropy</p>
    </div>
  </section>

  <div class="boardroom-photo" role="img" aria-label="Photo of a bright modern boardroom with consultants in business attire meeting around a conference table"></div>

  <h2 class="panel panel-dark heading who-title">Who We Are</h2>

  <div class="panel panel-light founded">
    <p>Founded in 2010 by Eleanor Ruth Vance Brennick, BCA was inspired by the national climate for stronger governance and deeper board engagement. Since then, we’ve worked with hundreds of board members to improve the impact of their philanthropic efforts.</p>
  </div>

  <div class="panel panel-dark team">
    <p>Our energetic and patient team of experts in nonprofit governance, operations and management will provide a comprehensive approach to problem solving, training and coaching. The result?</p>
    <p>Better Boards › Stronger Organizations › Greater Impact</p>
  </div>

  <div class="panel panel-light services">
    <p>BCA consultants will:</p>
    <ul>
      <li>Bring new perspectives and skills for strategic or generative (big picture) thinking</li>
      <li>Challenge your assumptions</li>
      <li>Offer innovative approaches to problem solving</li>
      <li>Identify sources of dysfunction</li>
      <li>Devise tactics to improve decision making or communication</li>
      <li>Make breakthrough improvements</li>
    </ul>
  </div>

  <h2 class="what-title">What we do</h2>

  <div class="panel panel-dark quote">
    <p>20th century developmental psychologist Henrik Alstrand asserted that for individuals, conflict and crisis are positive and necessary; they are “sources of growth, strength, and commitment.”</p>
  </div>

  <h3 class="panel panel-light heading org-label">Organizational<br>Clients</h3>

  <div class="panel panel-light believe">
    <p>We believe the same can be true of organizations. BCA helps nonprofits manage change and emerge triumphantly. Through coaching, we help organizations implement practices to maximize efficiency and effectiveness - whether preparing for transition, coping with chaos, or simply pursuing continued high performance - by working directly with board members and staff.</p>
    <p>Our methods are informed by research and honed by over 20 years of practice.</p>
  </div>

  <h3 class="panel panel-light heading private-label">Private Clients</h3>

  <div class="panel panel-dark individuals">
    <p>BCA philanthropic counsel helps individuals adopt impactful practices in their charitable endeavors.</p>
  </div>
</main>
</body>
</html>
```